Business Card Design

Mortgage brokering company, also providing Commercial Finance, Car Finance and Insurance.

Target Market(s)

Home Buyers

Industry/Entity Type

Business

Contact Information for Business Card

All information required on business card is contained in the attachment. Design does not have to follow the style of the attachment.

```html
<!DOCTYPE html>
<html lang="en">
<head>
<meta charset="utf-8">
<title>Kestrel Home Loans – Business Card</title>
<link rel="stylesheet" href="https://fonts.googleapis.com/css2?family=Arimo:wght@400;700&display=swap">
<style>
  :root {
    --backdrop: #2a2a2a;
    --card: #1c1c1c;
    --ink: #ffffff;
    --accent: #f7901e;
    --rule: #d9d9d9;
  }
  * { margin: 0; padding: 0; box-sizing: border-box; }
  html, body {
    width: 1200px; height: 900px; overflow: hidden;
    background: var(--backdrop);
    font-family: "Arimo", Arial, sans-serif;
    color: var(--ink);
  }
  .canvas { position: relative; width: 1200px; height: 900px; }
  .card {
    position: absolute; left: 280px;
    width: 640px; height: 390px;
    background: var(--card);
    overflow: hidden;
    box-shadow: 0 10px 30px rgba(0,0,0,.5);
  }
  .card--front { top: 45px; }
  .card--back { top: 465px; }

  /* brand: invented name set in the card's text face, one colour, one weight */
  .brand {
    display: flex; align-items: center; gap: 14px;
    white-space: nowrap;
  }
  .brand__mark {
    width: 18px; height: 18px;
    background: var(--accent);
    flex: none;
  }
  .brand__name {
    font-weight: 400;
    color: var(--ink);
    letter-spacing: 0.5px;
  }

  .card--front .brand {
    position: absolute; left: 50%; top: 140px; transform: translateX(-50%);
  }
  .card--front .brand__name { font-size: 40px; }
  .services {
    position: absolute; left: 0; right: 0; top: 275px;
    text-align: center;
    font-variant: small-caps; font-weight: 700;
    font-size: 24px; letter-spacing: 1.5px;
  }
  .services__sep { margin: 0 12px; }

  /* back */
  .card--back .brand {
    position: absolute; left: 40px; top: 160px;
  }
  .card--back .brand__name { font-size: 25px; }
  .card--back .brand__mark { width: 14px; height: 14px; }
  .divider {
    position: absolute; left: 345px; top: 20px;
    width: 1px; height: 300px;
    background: linear-gradient(var(--rule), rgba(217,217,217,0));
  }
  .contact { position: absolute; left: 372px; top: 30px; }
  .contact__name {
    font-variant: small-caps; font-weight: 700;
    font-size: 26px; letter-spacing: 1px;
  }
  .contact__role { color: var(--accent); font-size: 14px; margin-bottom: 24px; }
  .contact__list { list-style: none; font-size: 15px; line-height: 25px; }
  .contact__label { color: var(--accent); margin-right: 4px; }
  .contact__address { margin-top: 18px; font-size: 15px; line-height: 25px; }
  .band {
    position: absolute; left: 0; right: 0; bottom: 0; height: 38px;
    background: var(--accent);
  }
</style>
</head>
<body>
<main class="canvas">
  <section class="card card--front" aria-label="Card front">
    <div class="brand">
      <span class="brand__mark"></span>
      <span class="brand__name">Kestrel Home Loans</span>
    </div>
    <p class="services">Residential<span class="services__sep">|</span>Asset Finance<span class="services__sep">|</span>Insurance</p>
  </section>

  <section class="card card--back" aria-label="Card back">
    <div class="brand">
      <span class="brand__mark"></span>
      <span class="brand__name">Kestrel Home Loans</span>
    </div>
    <div class="divider"></div>
    <div class="contact">
      <h1 class="contact__name">Martin Hale</h1>
      <p class="contact__role">Credit Representative</p>
      <ul class="contact__list">
        <li><span class="contact__label">P:</span>07 5550 1234</li>
        <li><span class="contact__label">M:</span>0400 555 187</li>
        <li><span class="contact__label">F:</span>07 5550 1234</li>
        <li><span class="contact__label">E:</span>martin.hale@kestrelloans.com.au</li>
        <li><span class="contact__label">W:</span>www.kestrelloans.com.au</li>
      </ul>
      <p class="contact__address">14 Harbour View Road,<br>Broadbeach, Qld 4218</p>
    </div>
    <div class="band"></div>
  </section>
</main>
</body>
</html>
```